Personal Injury Lawyer Billboard

I would like a design created featuring the image of the lawyer centered in the middle of the design.
To the left of the lawyer's image it should read "INJURED?"
To the right of the lawyer's image, it should read "CALL DREW!"
Under Call Drew, include the phone number 318-555-0147.
At the bottom of the design include the lawyers information "Andrew Holloway Accident & Injury Lawyers"
PLEASE REMOVED THE BACKGROUND IMAGERY OF THE PHOTO SUBMITTED. Also, the colors for this design should match the colors shown in the logo (navy, white and relective soft gold). Please use those color combinations in ways that best stand out.

```html
<!DOCTYPE html>
<html lang="en">
<head>
<meta charset="utf-8">
<title>Andrew Holloway Accident &amp; Injury Lawyers – Billboard</title>
<link rel="stylesheet" href="https://fonts.googleapis.com/css2?family=Montserrat:wght@700;800;900&display=swap">
<style>
  :root {
    --navy: #0b1833;
    --navy-deep: #09152d;
    --gold: #df9b0c;
    --white: #ffffff;
    --photo-light: #dcdcdc;
    --photo-mid: #cfcfcf;
  }
  * { margin: 0; padding: 0; box-sizing: border-box; }
  html, body {
    width: 813px; height: 1200px; overflow: hidden;
    background: var(--navy);
  }
  .billboard {
    position: relative;
    width: 813px; height: 1200px;
    overflow: hidden;
    background: linear-gradient(180deg, var(--navy-deep) 0%, var(--navy) 100%);
    font-family: "Montserrat", Arial, sans-serif;
    color: var(--white);
  }
  .firm-name {
    position: absolute;
    top: 56px; right: 48px;
    width: 270px;
    text-align: right;
    font-weight: 800;
    font-size: 19px;
    line-height: 1.25;
    letter-spacing: 0.3px;
    color: var(--white);
    text-transform: uppercase;
  }
  .injured-tab {
    position: absolute;
    left: 0; top: 149px;
    width: 359px; height: 126px;
    background: var(--white);
    border-radius: 0 63px 63px 0;
    display: flex; align-items: center;
    padding-left: 48px;
  }
  .injured-tab span {
    font-weight: 800;
    font-size: 61px;
    letter-spacing: 1px;
    color: var(--navy-deep);
  }
  .call-line {
    position: absolute;
    right: 48px; top: 194px;
    font-weight: 800;
    font-size: 35px;
    letter-spacing: 0.5px;
    color: var(--white);
  }
  .phone {
    position: absolute;
    right: 47px; top: 240px;
    font-weight: 800;
    font-size: 59px;
    letter-spacing: -0.5px;
    color: var(--gold);
  }
  .portrait-frame {
    position: absolute;
    left: 0; top: 0;
    width: 813px; height: 1200px;
  }
  .name-pill {
    position: absolute;
    left: 101px; top: 849px;
    width: 611px; height: 119px;
    background: var(--gold);
    border-radius: 60px;
    display: flex; align-items: center; justify-content: center;
  }
  .name-pill span {
    font-weight: 900;
    font-size: 45px;
    letter-spacing: 0.5px;
    color: var(--white);
  }
  .practice {
    position: absolute;
    left: 0; top: 1012px;
    width: 813px;
    text-align: center;
    font-weight: 800;
    font-size: 50px;
    line-height: 64px;
    letter-spacing: 0.5px;
    color: var(--white);
  }
  .job-code {
    position: absolute;
    right: 43px; top: 1165px;
    font-size: 5px;
    font-weight: 700;
    color: var(--white);
  }
</style>
</head>
<body>
<main class="billboard">
  <div class="firm-name">Andrew Holloway<br>Accident &amp; Injury Lawyers</div>

  <div class="injured-tab"><span>INJURED</span></div>

  <div class="call-line">CALL DREW!</div>
  <div class="phone">318-555-0147</div>

  <svg class="portrait-frame" viewBox="0 0 813 1200" aria-hidden="false">
    <defs>
      <radialGradient id="photoTone" cx="50%" cy="45%" r="60%">
        <stop offset="0%" stop-color="var(--photo-light)"/>
        <stop offset="100%" stop-color="var(--photo-mid)"/>
      </radialGradient>
    </defs>
    <circle cx="406" cy="630" r="278" fill="url(#photoTone)" stroke="var(--gold)" stroke-width="10"
            role="img" aria-label="Portrait of lawyer Andrew Holloway in a navy suit and green tie, smiling with a raised fist, on a light grey background"/>
  </svg>

  <div class="name-pill"><span>ANDREW HOLLOWAY</span></div>

  <div class="practice">ACCIDENT &amp; INJURY<br>LAWYERS</div>

  <div class="job-code">C45</div>
</main>
</body>
</html>
```